Beautiful & Elegant Digital Brochure Needed For Luxury Real Estate Development

Hello,

Our company is seeking a beautiful design for our real estate development that is currently being launched.

About The Project:
Development Name - Harrow Mill Estate
Location - Charleston, S.C.
Low-Country Southern Style Architecture
Surfle "low-country" Charleston, SC to get an idea of the unique culture of the city
Surfle "copper birch tree" Charleston, SC to understand the branding

Other Digital Brochures that we love

http://www.vintrelodges.example/dunmerecove/wp-content/uploads/sites/6/2014/08/adventures-brochure.pdf

Why we like it... We love the classy feeling the brochure portrays by using unique fonts and backgrounds (burlap textures). We also love the images that represent a "low-country" vibe.

Requirements:
1. We will be providing all of the content (attached)

2. Please use plenty of southern low-country stock images from RapidLensPics (we have a subscription so just use the watermarked images unless you have full permissions)

3. Do not copy the Dunmere Cove brochure - create a unique vision that fits in to the low-country and southern vibe

4. Attached is our logos

The font we like to use is - Caslon Antique / italic
Thank you!

Target Market(s)

High net worth individuals - each homesite will be over 6 million dollars USD

Industry/Entity Type

Real Estate Development

Font styles to use
Script
Other font styles liked:
• Caslon Antique & Italic

Colors
abd036
00a990
acd036
9bcb3c
33b8a4
86cfc6
cfeae6

Requirements
Must have
• low country feeling
Nice to have
• burlap, wood backgrounds
Should not have
• Should NOT be corporate. This brochure is for multi-millionaire home buyers and investors. They are seeking simple, beautiful, quiet, serene, and southern lifestyles on the Intracoastal waterway on Wexley Cay, Charleston, South Carolina.

```html
<!DOCTYPE html>
<html lang="en">
<head>
<meta charset="utf-8">
<title>Harrow Mill Estate – Brochure Pages</title>
<link href="https://fonts.googleapis.com/css2?family=Cinzel:wght@400;500&family=Libre+Caslon+Text:ital@0;1&family=Marcellus&family=Arimo:wght@500&display=swap" rel="stylesheet">
<style>
  :root{
    --board:#c9c9c9;
    --ink-dark:#141414;
    --leather-1:#1d1d1d;
    --leather-2:#0c0c0c;
    --gold-deep:#8a6420;
    --gold-mid:#c99a34;
    --gold-light:#f4e390;
    --gold-text:#d9ad4a;
    --paper-1:#f4f4f3;
    --paper-2:#cfcfcd;
    --body-light:#e9e4d8;
    --body-dark:#2a2a2a;
    --label:#111;
  }
  *{box-sizing:border-box;margin:0;padding:0}
  html,body{width:902px;height:1200px;overflow:hidden}
  body{background:radial-gradient(ellipse at center,#e0e0e0 0%,var(--board) 75%);position:relative;font-family:"Libre Caslon Text",Georgia,serif}
  .board-label{position:absolute;width:378px;text-align:center;font-family:"Arimo",Arial,sans-serif;font-weight:500;font-size:22px;color:var(--label);letter-spacing:.3px}
  .page{position:absolute;width:378px;height:536px;overflow:hidden;box-shadow:0 3px 10px rgba(0,0,0,.45)}
  .page--dark{background:radial-gradient(ellipse at 50% 40%,var(--leather-1) 0%,var(--leather-2) 100%)}
  .page--light{background:linear-gradient(160deg,var(--paper-1) 0%,#e6e6e4 55%,var(--paper-2) 100%)}
  .gold-fill{background:linear-gradient(100deg,var(--gold-deep) 0%,var(--gold-light) 35%,var(--gold-mid) 70%,var(--gold-light) 100%)}
  .wordmark{position:absolute;left:0;width:100%;text-align:center;font-family:"Cinzel",serif;font-weight:400;color:var(--gold-text)}
  .wordmark__name{font-size:31px;letter-spacing:.5px;line-height:1}
  .wordmark__sub{font-size:12.5px;letter-spacing:5.5px;margin-top:7px;line-height:1}
  .cover__photo{position:absolute;left:0;top:182px}
  .cover__title{position:absolute;left:0;width:100%;text-align:center;font-family:"Marcellus",serif;color:var(--gold-text);font-size:23px;line-height:28px;letter-spacing:.3px;top:381px}
  .cover__city{position:absolute;left:0;width:100%;text-align:center;font-family:"Marcellus",serif;color:#f1f1f1;font-size:17px;top:445px}
  .cover__web{position:absolute;left:0;top:483px;width:100%;height:31px;text-align:center;font-size:13.5px;line-height:31px;color:#1b1407}
  .page-band{position:absolute;left:0;top:23px;width:100%;height:29px}
  .page-band::after{content:"";position:absolute;top:0;bottom:0;left:258px;width:58px;border-left:1px solid rgba(120,85,20,.45);border-right:1px solid rgba(120,85,20,.45)}
  .copy{position:absolute;left:34px;right:32px;top:68px;font-size:6.2px;line-height:9.9px;text-align:justify;hyphens:auto}
  .page--dark .copy{color:var(--body-light)}
  .page--light .copy{color:var(--body-dark)}
  .copy p{margin-bottom:9px}
  .copy h2{font-style:italic;font-weight:400;font-size:8.6px;line-height:11px;color:var(--gold-text);margin:13px 0 8px;text-transform:uppercase}
  .page--light .copy h2{color:#a7792a}
  .folio{position:absolute;left:0;bottom:0;width:100%;height:11px}
  .folio__line{position:absolute;left:0;right:0;bottom:3px;height:3px}
  .folio__num{position:absolute;left:50%;bottom:0;width:12px;height:12px;margin-left:-6px;border-radius:50%;font-size:6px;line-height:12px;text-align:center;color:#1b1407}
  .contact__photo{position:absolute;left:0;top:182px}
  .contact__panel{position:absolute;left:157px;top:182px;width:221px;height:177px;padding:38px 0 0 43px;color:#1a140a}
  .contact__heading{font-family:"Marcellus",serif;font-size:20px;letter-spacing:.3px;margin-bottom:11px}
  .contact__list{list-style:none;font-size:9.6px;line-height:15.4px}
  .contact__list svg{width:8px;height:8px;vertical-align:-1px;margin-right:4px}
</style>
</head>
<body>

<div class="board-label" style="left:65px;top:26px">COVER PAGE</div>
<div class="board-label" style="left:458px;top:26px">INNER PAGE 1</div>
<div class="board-label" style="left:65px;top:1154px">INNER PAGE 2</div>
<div class="board-label" style="left:458px;top:1154px">LAST PAGE</div>

<!-- Cover -->
<section class="page page--dark cover" style="left:65px;top:58px">
  <div class="wordmark" style="top:107px">
    <div class="wordmark__name">HARROW MILL</div>
    <div class="wordmark__sub">ESTATE</div>
  </div>
  <svg class="cover__photo" width="378" height="177" viewBox="0 0 378 177">
    <defs>
      <linearGradient id="coverGold" x1="0" y1="0" x2="1" y2="1">
        <stop offset="0" stop-color="#8a6420"/><stop offset=".45" stop-color="#f4e390"/><stop offset="1" stop-color="#b8862c"/>
      </linearGradient>
      <linearGradient id="coverScene" x1="0" y1="0" x2="0" y2="1">
        <stop offset="0" stop-color="#e7a98f"/><stop offset=".35" stop-color="#d9cfc4"/><stop offset=".7" stop-color="#6f7a5a"/><stop offset="1" stop-color="#3d4a2c"/>
      </linearGradient>
    </defs>
    <rect x="0" y="0" width="10" height="177" fill="url(#coverGold)"/>
    <polygon points="17,0 327,0 287,177 17,177" fill="url(#coverScene)" role="img" aria-label="Photo of a white low-country mansion behind a tiered pineapple fountain at dusk"/>
    <polygon points="338,0 378,0 378,177 298,177" fill="url(#coverGold)"/>
  </svg>
  <h1 class="cover__title">LOW-COUNTRY SOUTHERN<br>STYLE ARCHITECTURE</h1>
  <div class="cover__city">CHARLESTON, S.C.</div>
  <div class="cover__web gold-fill">www.websiteaddress.com</div>
</section>

<!-- Inner page 1 -->
<section class="page page--dark" style="left:458px;top:58px">
  <div class="page-band gold-fill"></div>
  <div class="copy">
    <p>Nestled on pristine Wexley Cay, the Harrow Mill Estate Community is a truly enviable locale. An unspoiled maritime forest and the island's meandering coastline create a stunning natural backdrop while proximity to Charleston's world-class dining and superior shops means that you never have to sacrifice comfort or style. Within the community, eighteen large, private home sites offer ample space to gather in an intimate setting with family and friends while the forty acre common area provides space for large gatherings and community events. Private pools, equestrian activities, racquet sports, and golfing are among the many community-based amenities that will connect you to your neighbors. Whether you seek a peaceful escape for deep relaxation, to adopt the spirit of Southern hospitality, or to immerse yourself in the Lowcountry experience, Harrow Mill Estate is the perfect haven.</p>
    <h2>The Legend of the Copper Birch</h2>
    <p>The community is named for South Carolina's enchanting copper birch tree, a centuries-old tree located at the heart of Wexley Cay. Although the exact age of the tree is unknown, estimates based on the tree's size and condition suggest that it is between 700 and 1500 years old. The tree predates recorded history on the island and likely stood its ground long before the arrival of Admiral Corwen Vale to the Americas. The ancient tree's massive, sprawling branches reach outward in all directions, covering more than 17,000 square feet of ground with its majestic shade. Standing more than 65 feet tall, it towers over the park that bears its name. This imposing beauty has become one of the area's most iconic natural wonders, drawing thousands of visitors each year. Situated amid a treasure trove of historic structures and man-made beauty, the park offers visitors a reminder of Mother Nature's strength, vitality, and splendor.</p>
    <h2>Embrace Outdoor Living and Connect with Nature</h2>
    <p>Life is better when lived outdoors and in the Lowcountry, nature beckons. Wake each morning to breathtaking sunrises and allow the warm, salt-kissed air to rejuvenate your soul. Spend your days enjoying one of the area's exquisite beaches or visit some of Charleston's inspiring heritage sites. During the early evenings, enjoy dinner alfresco before retiring on the veranda with family and friends. Gather around an outdoor fireplace to share the day's memories and create even more under the stars.</p>
    <p>Featuring both community and private docks, Harrow Mill is a maritime paradise. Board your vessel to explore the tidal Stono River separating Wexley Cay from the mainland or follow the Intracoastal Waterway to the sea. For the adventurous, a kayak or canoe is an ideal means for exploring the intricacies of the island's elaborate coastal marshes. Sport fishers will be pleased to find the channels teeming with flounder, cobia, mackerel, tarpon, white shrimp, and blue crabs. Non-anglers will also appreciate the plentiful array of aquatic life and availability of fresh daily seafood.</p>
    <p>Inland, Charleston County is home to stunning city gardens, immaculate local parks, and quaint nature trails. Terrestrial wildlife is plentiful on the island and even a short hike is likely to yield amazing photo opportunities. The island is heavily populated by South Carolina's state animal, the white tailed deer, which can be seen bounding through the wooded terrain year-round. Wild turkeys, gray fox, flying squirrels, raccoon, bobcats, and bear also call the island home. For bird watchers, a close eye on the skies will yield handsome rewards. Heron, osprey, bald eagles, red-tailed hawks, egrets, and wood storks all call the island home. Dozens of migratory species provide increased variety to an already impressive host of island regulars and are always a welcome herald to the changing seasons.</p>
  </div>
  <div class="folio"><div class="folio__line gold-fill"></div><div class="folio__num gold-fill">1</div></div>
</section>

<!-- Inner page 2 -->
<section class="page page--light" style="left:65px;top:611px">
  <div class="page-band gold-fill"></div>
  <div class="copy">
    <p>Despite seeing an influx of visitors and new residents, a strong commitment to ecologically conscious growth promises that this natural wonderland will remain intact for generations to come. Coastal management, wildlife conservation, and the protection of the area's natural resources are paramount among the considerations and development is conducted responsibly and respectfully.</p>
    <h2>Welcome to the Lowcountry,<br>Where Tradition and Elegance Meet.</h2>
    <p>Charleston has always embodied the geniality of the aristocratic South and has been a conspicuous epicenter for some of the country's finest art, architecture, and cultural resources. This is flawlessly illustrated by the concentration of exquisite historic structures located throughout the city and the surrounding countryside. The city's architectural heritage has been nurtured by many groups including Charleston's active and influential Preservation Society. The group, founded in 1920, is the oldest of its kind anywhere in the country. Owing to their ongoing efforts, the city's National Historic Landmark District has seen multiple expansions as restoration projects have materialized throughout the area. The group is committed to promoting the city's historical legacy through restorative projects, preservation initiatives, and education about the city's rich heritage.</p>
    <p>With new additions to the Historic Registry as recently as the 1980s, the city's ever-growing designated "Old and Historic District" has now expanded to cover 138 acres. Within these borders, nearly 5000 exquisitely preserved historic buildings stand as testament to the city's dedication to maintaining the beautiful architecture in and around the heart of the city. Picturesque examples from an array of architectural periods line city streets, beckoning tourists and inspiring awe in passers-by. Georgian, Regency, and Federal, as well as Classical, Greek, and Gothic Revivals are some of the more popular and most prominently featured styles but the city is host to many homes, shops, and civic buildings whose designs were inspired by other periods of architectural influence.</p>
    <p>While many buildings are being rehabilitated throughout the city, conservation efforts are also dedicated to preventing the further decline of surviving historic sites. Efforts to preserve original structures and their components have been hugely successful. Throughout the city, stunning historical features in pristine condition stand as a testament to dedicated conservators' efforts. Perhaps the most notable example is that some area homes still proudly feature their original crown glass windows, remarkably intact after hundreds of years. The antique glass was traditionally hand-blown by highly skilled artisans aided by experienced assistants. Due to the irregularities in thickness and density, the method resulted in a distinct, wavy optical quality that can be easily identified by the discerning eye.</p>
    <h2>New Meets Old</h2>
    <p>The Lowcountry boasts a proud tradition of refined Southern grace and charming appeal. Few cities have been able to blend this heirloom charm with modernity quite like Charleston, which has become a premium destination for those seeking to abandon the drab, predictable regularity that characterizes modern existence. For decades, the city has continually expanded, acquiring nearby land and enticing new residents seeking a diversion from the ordinary. While encouraging this growth, the city, local government, and residents remain steadfastly dedicated to maintaining the time-honored elegance of historic Charleston.</p>
  </div>
  <div class="folio"><div class="folio__line gold-fill"></div><div class="folio__num gold-fill">2</div></div>
</section>

<!-- Last page -->
<section class="page page--dark" style="left:458px;top:611px">
  <svg class="contact__photo" width="147" height="177" viewBox="0 0 147 177" role="img" aria-label="Photo of pastel Charleston row houses with palmetto trees under a blue sky">
    <defs>
      <linearGradient id="contactScene" x1="0" y1="0" x2="0" y2="1">
        <stop offset="0" stop-color="#2f6fc4"/><stop offset=".4" stop-color="#c9c28a"/><stop offset=".75" stop-color="#6d7a3c"/><stop offset="1" stop-color="#2e3a1e"/>
      </linearGradient>
    </defs>
    <rect width="147" height="177" fill="url(#contactScene)"/>
  </svg>
  <div class="contact__panel gold-fill">
    <h2 class="contact__heading">CONTACT US:</h2>
    <ul class="contact__list">
      <li><svg viewBox="0 0 10 10"><path d="M5 0.5a3.3 3.3 0 0 1 3.3 3.3C8.3 6.2 5 9.5 5 9.5S1.7 6.2 1.7 3.8A3.3 3.3 0 0 1 5 .5z" fill="none" stroke="#1a140a" stroke-width="1.2"/><circle cx="5" cy="3.8" r="1.1" fill="#1a140a"/></svg>Address Goes Here</li>
      <li><svg viewBox="0 0 10 10"><path d="M2 .8l1.8 1.9-.9 1.4c.6 1.3 1.7 2.4 3 3l1.4-.9L9.2 8 8 9.3C4.4 9 1 5.6.7 2z" fill="#1a140a"/></svg>Phone Number Goes Here</li>
      <li><svg viewBox="0 0 10 10"><rect x="2.5" y=".8" width="5" height="3" fill="none" stroke="#1a140a"/><rect x=".8" y="3.6" width="8.4" height="4.2" rx=".6" fill="#1a140a"/><rect x="2.5" y="6.5" width="5" height="2.7" fill="#1a140a"/></svg>Fax Number Goes Here</li>
      <li><svg viewBox="0 0 10 10"><rect x=".8" y="2" width="8.4" height="6" fill="none" stroke="#1a140a"/><path d="M.8 2L5 5.6 9.2 2" fill="none" stroke="#1a140a"/></svg>E-mail Id Goes Here</li>
      <li><svg viewBox="0 0 10 10"><circle cx="5" cy="5" r="4.2" fill="none" stroke="#1a140a"/><ellipse cx="5" cy="5" rx="1.8" ry="4.2" fill="none" stroke="#1a140a" stroke-width=".8"/><path d="M.8 5h8.4" stroke="#1a140a" stroke-width=".8"/></svg>Website Goes Here</li>
    </ul>
  </div>
  <div class="wordmark" style="top:449px">
    <div class="wordmark__name" style="font-size:28px">HARROW MILL</div>
    <div class="wordmark__sub" style="font-size:11.5px;letter-spacing:5px">ESTATE</div>
  </div>
</section>

</body>
</html>
```